Private Learning Centre in Singapore needs a flyer design

We need a flyer design for our upcoming education fair and also able to use it for day to day purpose. The aim is to attract parents, students to enrol for classes by offering them free trial class/assessment. 2 sided flyer with the front page as the logo only and details on the other page. We would like to see a final design in blue, white and it should be curious and attractive enough not to allow customers to throw it away once they received it.

Education

```html
<!DOCTYPE html>
<html lang="en">
<head>
<meta charset="utf-8">
<title>Bright Path Academy – Flyer</title>
<link rel="stylesheet" href="https://fonts.googleapis.com/css2?family=PT+Sans+Narrow:wght@700&family=Source+Sans+3:wght@400;600;700&display=swap">
<style>
  :root {
    --backdrop: #1e1e1e;
    --brand-blue: #3a52a6;
    --brand-blue-deep: #34499a;
    --paper: #ffffff;
    --paper-shade: #dedede;
    --ink: #555555;
    --ink-dark: #333333;
    --muted: #a0a0a0;
    --sweep: #c9d4f0;
  }
  * { box-sizing: border-box; margin: 0; padding: 0; }
  html, body { width: 1200px; height: 1000px; overflow: hidden; }
  body {
    background: var(--backdrop);
    font-family: "Source Sans 3", "Helvetica Neue", Arial, sans-serif;
    position: relative;
  }

  .flyer-side {
    position: absolute;
    top: 150px;
    width: 495px;
    height: 680px;
    overflow: hidden;
  }

  /* Front */
  .flyer-front {
    left: 66px;
    background:
      radial-gradient(ellipse 55% 35% at 55% 42%, rgba(120,165,235,0.5), rgba(120,165,235,0) 70%),
      linear-gradient(160deg, var(--brand-blue) 0%, var(--brand-blue-deep) 100%);
  }
  .front-brand {
    position: absolute;
    left: 0; right: 0;
    top: 220px;
    display: flex;
    flex-direction: column;
    align-items: center;
    gap: 22px;
  }
  .front-brand-mark {
    width: 120px; height: 120px;
    border-radius: 50%;
    background: var(--paper);
  }
  .front-brand-name {
    color: var(--paper);
    font-weight: 600;
    font-size: 28px;
    letter-spacing: 3px;
    text-transform: uppercase;
  }
  .front-website {
    position: absolute;
    left: 0; right: 0;
    top: 635px;
    text-align: center;
    color: var(--paper);
    font-size: 11px;
    letter-spacing: 2.6px;
  }

  /* Back */
  .flyer-back {
    left: 613px;
    background: linear-gradient(180deg, var(--paper) 0%, var(--paper) 50%, var(--paper-shade) 100%);
  }
  .back-top-band {
    position: absolute; left: 0; top: 0;
    width: 100%; height: 6px;
    background: var(--brand-blue);
  }
  .back-light-sweep {
    position: absolute; left: 0; top: 6px;
    width: 495px; height: 100px;
  }
  .offer-headline {
    position: absolute; left: 55px; top: 60px;
    font-family: "PT Sans Narrow", "Arial Narrow", sans-serif;
    font-weight: 700;
    font-size: 92px;
    line-height: 1;
    color: var(--brand-blue);
    letter-spacing: -2px;
  }
  .offer-subline {
    position: absolute; left: 58px; top: 138px;
    font-weight: 600;
    font-size: 24px;
    letter-spacing: 0.5px;
    color: var(--muted);
  }
  .intro-title {
    position: absolute; left: 56px; top: 225px;
    font-weight: 700;
    font-size: 15px;
    color: var(--brand-blue);
  }
  .intro-text {
    position: absolute; left: 56px; top: 252px;
    width: 392px;
    font-size: 11.4px;
    line-height: 25px;
    color: var(--ink);
  }
  .back-brand {
    position: absolute; left: 56px; top: 392px;
    display: flex; align-items: center; gap: 8px;
  }
  .back-brand-mark {
    width: 40px; height: 40px; border-radius: 50%;
    background: var(--brand-blue);
  }
  .back-brand-name {
    font-weight: 600; font-size: 10px;
    color: var(--brand-blue);
    text-transform: uppercase;
    letter-spacing: 1px;
    width: 80px; line-height: 1.3;
  }
  .stairs-visual {
    position: absolute; left: 20px; top: 425px;
    width: 460px; height: 240px;
  }
  .contact-block {
    position: absolute; right: 90px; top: 598px;
    text-align: right;
    font-style: normal;
    font-size: 10.5px;
    line-height: 13px;
    color: var(--ink-dark);
  }
  .contact-name { font-weight: 700; }
  .social-link {
    position: absolute; left: 416px; top: 604px;
    display: flex; flex-direction: column; align-items: center; gap: 2px;
  }
  .social-mark {
    width: 36px; height: 36px;
    border-radius: 3px;
    background: var(--brand-blue);
  }
  .social-name {
    font-size: 9px; font-weight: 600; color: var(--brand-blue);
  }
</style>
</head>
<body>

  <section class="flyer-side flyer-front" aria-label="Flyer front">
    <div class="front-brand">
      <div class="front-brand-mark"></div>
      <div class="front-brand-name">Bright Path Academy</div>
    </div>
    <p class="front-website">www.brightpathacademy.com</p>
  </section>

  <section class="flyer-side flyer-back" aria-label="Flyer back">
    <div class="back-top-band"></div>
    <svg class="back-light-sweep" viewBox="0 0 495 100" aria-hidden="true">
      <defs>
        <linearGradient id="sweepFade" x1="0" y1="0" x2="1" y2="0">
          <stop offset="0" stop-color="#c9d4f0" stop-opacity="0"/>
          <stop offset="0.5" stop-color="#c9d4f0" stop-opacity="0.8"/>
          <stop offset="1" stop-color="#c9d4f0" stop-opacity="0.3"/>
        </linearGradient>
      </defs>
      <path d="M220 0 C320 20 420 50 495 70 L495 90 C410 60 320 25 220 0 Z" fill="url(#sweepFade)"/>
      <path d="M250 0 C340 25 430 55 495 82" stroke="url(#sweepFade)" stroke-width="1.5" fill="none"/>
      <path d="M280 0 C360 18 440 40 495 55" stroke="url(#sweepFade)" stroke-width="1" fill="none"/>
    </svg>

    <h1 class="offer-headline">FREE</h1>
    <p class="offer-subline">TRIAL CLASS</p>

    <h2 class="intro-title">Introduction</h2>
    <p class="intro-text">Bright Path Academy is where you can develop academic and life skills. Our teachers are the heartbeat of the business. They inspire and nurture students, helping them surpass their expectations. We cover English, Mathematics and Science from Primary and Secondary Levels.</p>

    <div class="back-brand">
      <div class="back-brand-mark"></div>
      <div class="back-brand-name">Bright Path Academy</div>
    </div>

    <svg class="stairs-visual" viewBox="0 0 460 240" role="img" aria-label="White floating steps rising to the right against a soft grey wall">
      <defs>
        <radialGradient id="stairsGlow" cx="0.55" cy="0.55" r="0.6">
          <stop offset="0" stop-color="#d2d2d2" stop-opacity="0.7"/>
          <stop offset="0.6" stop-color="#dcdcdc" stop-opacity="0.35"/>
          <stop offset="1" stop-color="#e6e6e6" stop-opacity="0"/>
        </radialGradient>
        <linearGradient id="stairsBand" x1="0" y1="1" x2="1" y2="0">
          <stop offset="0" stop-color="#ffffff" stop-opacity="0.9"/>
          <stop offset="1" stop-color="#f4f4f4" stop-opacity="0.9"/>
        </linearGradient>
      </defs>
      <rect width="460" height="240" fill="url(#stairsGlow)"/>
      <path d="M0 225 L440 10 L450 30 L20 235 Z" fill="url(#stairsBand)" opacity="0.7"/>
    </svg>

    <address class="contact-block">
      <div class="contact-name">Bright Path Academy</div>
      <div>118 Seaview Lane 428901</div>
      <div>6210 4477</div>
      <div>hello@brightpathacademy.com</div>
    </address>

    <div class="social-link">
      <div class="social-mark"></div>
      <span class="social-name">Chatter</span>
    </div>
  </section>

</body>
</html>
```